crumbs of morning project

I need 2 stickers (lid and side) for a see-through rectangular plastic container that holds a whole, free range chicken.
Updates

CHANGE OF PACKAGING

 

we are unable to source the clear, rectangular, see-throughcontainer in the previously attached file and have to amend our packagingstrategy.

 

 

 

UPDATED STRATEGY:

 

we intend to use one of the 'french style' cardboard typewrap-around stickers as shown in the new attachments I have posted. australiansupermarkets would not accept this type of thin cardboard on its own as is applicablein france and for that reason we intend insert the wrapped-around cardboard stickeredwhole chicken on a poly styrene tray and then placed in a clear plastic cellophanebag with a twisted tie as shown the 'varnot brand' attached file.

 

the other technical requirements (barcode, kilograms, netpricing, etc.) remain the same

 

 

also note:

 

when using our existing 'seal pure' logo, please removethe text:

 

rabbi tovah lindquist haber

potential brand names:

1. crumbs of morning
2. brisk olando

cardboard label needs to be a ' wrap around label' (wrapped, north-south) as shown in the following 
attached files:

'wrap around label'  + 'wrap around label b'

we like the 'brisk olando' FONT and primary yellow background. 

dorvid 

Target Market(s)

free range poultry consumers (GREENIES) jews (seal pure), affluent, up market, product is priced at the premium end of the market

Industry/Entity Type

Plastic

Requirements
Must have
• in order of importance...

LID LABEL STICKER-(see attached photo)
logo name (crumbs of morning)
free range
sanitised with kosher rock salt
extra fresh
long shelf life
kosher certified

SIDE LABEL STICKER- (see attached photo)
country of manufacture
processors contact details
(7 pellbrook lane ashvale west 3290 0487 220 318 www.crumbsofmorning.com.au)
barcode
product description (whole, drumsticks, filets, etc)
kosher status declaration and kosher logo (see attachment)
price per kilogram section
net weight per kilogram section
use by date
total price
refrigeration advise-store below 5degreesC

note:

the whole chicken is wrapped in light BROWN colored butchers paper and tied with a green ribbon. the customer can only see the raw chicken at each end.

```html
<!DOCTYPE html>
<html lang="en">
<head>
<meta charset="utf-8">
<title>Crumbs of Morning – Lid Label</title>
<link href="https://fonts.googleapis.com/css2?family=Amaranth:ital,wght@0,700;1,400;1,700&display=swap" rel="stylesheet">
<style>
  :root {
    --page: #ffffff;
    --egg-fill: #540b02;
    --egg-rim: #3d0f0a;
    --ink: #ffffff;
  }
  html, body {
    margin: 0;
    padding: 0;
    width: 1008px;
    height: 1200px;
    overflow: hidden;
    background: var(--page);
  }
  .label {
    position: relative;
    width: 1008px;
    height: 1200px;
    font-family: "Amaranth", "Trebuchet MS", sans-serif;
    font-style: italic;
    font-weight: 400;
    color: var(--ink);
  }
  .label__egg {
    position: absolute;
    inset: 0;
  }
  .brand {
    position: absolute;
    left: 0;
    right: 0;
    text-align: center;
    margin: 0;
    font-weight: 700;
    line-height: 1;
  }
  .brand__top { top: 190px; font-size: 82px; font-style: italic; }
  .brand__main { top: 268px; font-size: 122px; font-style: normal; letter-spacing: 0; }

  .claims {
    position: absolute;
    left: 0;
    right: 0;
    top: 486px;
    margin: 0;
    padding: 0;
    list-style: none;
    text-align: center;
    font-size: 80px;
    line-height: 89px;
  }
  .claims li { white-space: nowrap; }
  .arrow-left::before,
  .arrow-right::after {
    content: "";
    display: inline-block;
    vertical-align: middle;
    border-top: 8px solid transparent;
    border-bottom: 8px solid transparent;
    position: relative;
    top: -4px;
  }
  .arrow-left::before {
    border-right: 24px solid var(--ink);
    margin-right: 14px;
  }
  .arrow-right::after {
    border-left: 24px solid var(--ink);
    margin-left: 14px;
  }
</style>
</head>
<body>
<main class="label">
  <svg class="label__egg" width="1008" height="1200" viewBox="0 0 1008 1200" aria-hidden="true">
    <path d="M511,56 C720,56 941,480 941,731 C941,980 750,1155 511,1155 C272,1155 81,980 81,731 C81,480 302,56 511,56 Z"
          fill="var(--egg-fill)" stroke="var(--egg-rim)" stroke-width="18"/>
    <g class="divider" fill="var(--ink)">
      <polygon points="200,429 474,424 478,429 474,434"/>
      <polygon points="822,429 548,424 544,429 548,434"/>
      <polygon points="470,421 480,429 470,437 478,429"/>
      <polygon points="552,421 542,429 552,437 544,429"/>
      <polygon points="511,415 525,429 511,443 497,429"/>
    </g>
  </svg>

  <h1 class="brand brand__top">Crumbs of</h1>
  <p class="brand brand__main">morning</p>

  <ul class="claims">
    <li class="arrow-left arrow-right">Free range</li>
    <li class="arrow-left">Sanitised with</li>
    <li class="arrow-right">kosher rock salt</li>
    <li class="arrow-left arrow-right">Extra fresh</li>
    <li class="arrow-left arrow-right">Long shelf life</li>
    <li class="arrow-left arrow-right">Kosher certified</li>
  </ul>
</main>
</body>
</html>
```